Creative Out of the Box Post Up Banner Needed

I am looking for a great design for my banner. The design will be printed on a retractable vertical banner. Size 80 inches X 32 inches.

It will be displayed at my seminar and industry trade shows.

It needs to position me as a celebrity expert to grab people's attention. It shouldn't look boring.

Imagine a banner for a celebrity or a rock star.

It should look high-end and elegant.

The banner should include the entire body from head to toe, that makes it life-size when I print the banner.

Target Market(s)

salon and spa owners

Industry/Entity Type

Industry

Requirements
Must have
• My photo and a small book cover image.

You can download the images from:
http://www.glowtradecoach.com/images/bannerphoto.jpg
http://www.glowtradecoach.com/images/bookcover.jpg

Text that on the banner.

"Successful, rich, happy owners aren't smarter. They just play by a different set of rules."

Ivo Venn
#1 Business Expert In The Salon & Spa Industry
Millionaire Salon Owner
Best-Selling Author of Quiet Habits Of Parlor Keepers And A Ladder Out Of Debt
Nice to have
• Designs that I like.
http://www.artpitchhub.com/design/69852/poster-design-other-by-lumenpixo
http://mint-lantern.co.kr/pds/board/201108/poster.jpg
http://herbookedchairs.com/wp-content/uploads/2009/11/P10101561.jpg

```html
<!DOCTYPE html>
<html lang="en">
<head>
<meta charset="utf-8">
<title>Ivo Venn – Retractable Banner</title>
<link href="https://fonts.googleapis.com/css2?family=Roboto+Slab:wght@700;800;900&family=Arimo:ital,wght@0,700;1,700&display=swap" rel="stylesheet">
<style>
  :root {
    --sky-top: #3f5568;
    --sky-mid: #7d93a8;
    --sky-low: #b7c9d8;
    --floor: #dfe9f1;
    --ray: rgba(255,255,255,0.10);
    --quote-white: #ffffff;
    --name-ink: #16202a;
    --credential-ink: #1d3550;
    --suit-dark: #17181c;
    --suit-mid: #34373e;
    --book-green: #7fa54a;
    --book-light: #f2f2ec;
  }
  * { margin: 0; padding: 0; box-sizing: border-box; }
  html, body { width: 1200px; height: 2988px; overflow: hidden; }
  body {
    position: relative;
    background: linear-gradient(180deg, var(--sky-top) 0%, var(--sky-mid) 20%, var(--sky-low) 50%, var(--floor) 85%, #f3f7fa 100%);
    font-family: "Arimo", Arial, sans-serif;
  }
  .light-rays {
    position: absolute; inset: 0 0 auto 0; height: 1100px;
    background: repeating-linear-gradient(180deg, var(--ray) 0 18px, transparent 18px 46px);
    -webkit-mask-image: linear-gradient(180deg, #000 0%, transparent 100%);
            mask-image: linear-gradient(180deg, #000 0%, transparent 100%);
  }
  .floor-glow {
    position: absolute; left: 0; right: 0; top: 2500px; height: 488px;
    background: radial-gradient(ellipse at 65% 40%, rgba(255,255,255,0.85), transparent 65%);
  }
  .portrait {
    position: absolute; left: 560px; top: 450px; width: 540px; height: 2480px;
    border-radius: 220px 220px 80px 80px;
    background: linear-gradient(180deg, var(--suit-mid) 0%, var(--suit-dark) 25%, var(--suit-dark) 90%, var(--suit-mid) 100%);
    z-index: 1;
  }
  .quote {
    position: absolute; left: 40px; top: 40px; width: 1140px; z-index: 2;
    font-family: "Roboto Slab", Georgia, serif; font-weight: 900;
    color: var(--quote-white);
    text-shadow: 0 4px 12px rgba(0,0,0,0.45);
    line-height: 1;
  }
  .quote .q1 { font-size: 160px; letter-spacing: -3px; }
  .quote .q2 { font-size: 200px; margin-left: 100px; margin-top: -10px; }
  .quote .q3 { font-size: 64px; margin-left: 240px; margin-top: 30px; font-weight: 800; }
  .quote .q4 { font-size: 60px; margin-left: 240px; margin-top: 4px; font-weight: 800; }
  .quote .q5 { font-size: 44px; margin-left: 240px; margin-top: 10px; font-weight: 700; line-height: 1.12; }
  .quote .q5 .rules { display: block; margin-left: 40px; }
  .book {
    position: absolute; width: 200px; height: 430px; z-index: 2;
    background: linear-gradient(180deg, var(--book-light) 0%, var(--book-light) 80%, var(--book-green) 80%);
    border: 3px solid var(--book-green);
    box-shadow: 6px 8px 18px rgba(0,0,0,0.3);
  }
  .book.back { left: 24px; top: 960px; }
  .book.front { left: 60px; top: 990px; }
  .expert-name {
    position: absolute; left: 70px; top: 1520px; z-index: 2;
    font-family: "Roboto Slab", Georgia, serif; font-weight: 800;
    font-size: 48px; color: var(--name-ink);
  }
  .expert-title {
    position: absolute; left: 70px; top: 1590px; z-index: 2;
    font-weight: 700; font-size: 38px; color: var(--name-ink); line-height: 1.2;
  }
  .credentials {
    position: absolute; left: 70px; top: 1840px; width: 520px; z-index: 2;
    font-weight: 700; font-size: 38px; line-height: 1.22; color: var(--credential-ink);
  }
  .credentials .book-title { font-style: italic; }
</style>
</head>
<body>
  <div class="light-rays"></div>
  <div class="floor-glow"></div>

  <div class="portrait" role="img" aria-label="Full-length photo of Ivo Venn standing in a dark suit, arms crossed, legs crossed"></div>

  <div class="quote">
    <div class="q1">"Successful,</div>
    <div class="q2">rich,</div>
    <div class="q3">happy owners</div>
    <div class="q4">aren't smarter.</div>
    <div class="q5">They just play<span class="rules">by a different set of rules."</span></div>
  </div>

  <div class="book back" role="img" aria-label="Book cover of Quiet Habits Of Parlor Keepers And A Ladder Out Of Debt"></div>
  <div class="book front" role="img" aria-label="Book cover of Quiet Habits Of Parlor Keepers And A Ladder Out Of Debt"></div>

  <div class="expert-name">Ivo Venn</div>
  <div class="expert-title">#1 Business<br>Expert</div>

  <div class="credentials">
    In The Salon<br>
    &amp; Spa Industry<br>
    Millionaire<br>
    Salon Owner<br>
    Best-Selling Author<br>
    of <span class="book-title">Quiet Habits Of Parlor<br>
    Keepers And A Ladder<br>
    Out Of Debt</span>
  </div>
</body>
</html>
```